Business Card Design for Varnok Facility Services

We are looking for a Business Card Design for the Company "Varnok Facility Services."
Front side:
- Company Logo (small)
- Company Name, address, pohone, website and personal data.
- white background, for text e.g. company colors (blue or green like in the logo)
Please use following data:
Company data:
Varnok Facility Services Tulbrecht
Kirchmattweg 12
6331 Cham
www.varnok-fs.ch
Person data:
Ruben Tulbrecht
Geschäftsführer
+41 76 519 84 60
info@varnok-fs.ch
Back side:
could be colored in blue or green
please use a big logo sing and some smaller icons to say what is all beeing offered in facility services, like cleaning, maintenance cleaning
industrial cleaning, caretaking, gardening, disposal. There is no need for everyone of the icons if there are similar or an icon is standing for more of them.
Cleaning Service
colors to use:
blue: HEX 246BB0
green: HEX 52B33E

```html
<!DOCTYPE html>
<html lang="de">
<head>
<meta charset="utf-8">
<title>Varnok Facility Services – Business Card</title>
<link rel="stylesheet" href="https://fonts.googleapis.com/css2?family=Poppins:wght@400;500;600&display=swap">
<style>
  :root {
    --brand-blue: #246bb0;
    --name-blue: #0a57b3;
    --back-blue: #0050b0;
    --brand-green: #52b33e;
    --icon-green: #7dc242;
    --text-grey: #4a4a4a;
    --page: #eceae6;
    --card-white: #ffffff;
  }
  * { margin: 0; padding: 0; box-sizing: border-box; }
  html, body {
    width: 1125px; height: 1200px; overflow: hidden;
    background: var(--page);
    font-family: "Poppins", sans-serif;
  }
  .canvas { position: relative; width: 1125px; height: 1200px; }

  .card {
    position: absolute; left: 150px; width: 825px; height: 470px;
    box-shadow: 0 3px 8px rgba(0,0,0,0.25);
    overflow: hidden;
  }
  .card-front { top: 99px; background: var(--card-white); }
  .card-back { top: 632px; background: var(--back-blue); }

  .person-name {
    position: absolute; left: 41px; top: 159px;
    font-size: 30px; font-weight: 600; color: var(--name-blue); line-height: 1;
  }
  .person-role {
    position: absolute; left: 41px; top: 197px;
    font-size: 20px; font-weight: 400; color: var(--brand-green); line-height: 1;
  }
  .contact-list {
    position: absolute; left: 42px; top: 246px; list-style: none;
    font-size: 20px; color: var(--text-grey); line-height: 26px;
  }
  .contact-list li { display: flex; align-items: center; gap: 10px; }
  .contact-list svg { width: 17px; height: 17px; fill: var(--name-blue); flex: none; }
  .company-address {
    position: absolute; left: 41px; top: 348px;
    font-size: 20px; color: var(--text-grey); line-height: 25px; font-style: normal;
  }
  .emblem-area {
    position: absolute; left: 382px; top: 0; width: 443px; height: 440px;
    background: linear-gradient(135deg, rgba(36,107,176,0.18), rgba(82,179,62,0.22));
    border-bottom-left-radius: 440px 90px;
  }

  .brand-name {
    position: absolute; left: 0; right: 0; top: 148px; text-align: center;
    font-size: 46px; font-weight: 500; color: var(--card-white); letter-spacing: 1px;
  }
  .service {
    position: absolute; top: 312px; width: 130px; margin-left: -65px;
    text-align: center; color: var(--icon-green); font-size: 17px; line-height: 21px;
  }
  .service-icon {
    display: block; width: 78px; height: 78px; margin: 0 auto 14px;
    border: 2px solid var(--icon-green); border-radius: 50%;
    padding: 13px;
  }
  .service-icon svg { display: block; width: 100%; height: 100%; fill: var(--icon-green); }
</style>
</head>
<body>
<div class="canvas">

  <section class="card card-front">
    <div class="emblem-area" role="img" aria-label="Company emblem decoration area"></div>
    <h1 class="person-name">Ruben Tulbrecht</h1>
    <p class="person-role">Geschäftsführer</p>
    <ul class="contact-list">
      <li><svg viewBox="0 0 16 16"><path d="M4 0h8a1.5 1.5 0 0 1 1.5 1.5v13A1.5 1.5 0 0 1 12 16H4a1.5 1.5 0 0 1-1.5-1.5v-13A1.5 1.5 0 0 1 4 0zm0 2v10.5h8V2zm4 11.3a.9.9 0 1 0 0 1.8.9.9 0 0 0 0-1.8z"/></svg>+41 76 519 84 60</li>
      <li><svg viewBox="0 0 16 16"><path d="M0 3h16v10H0zm1.5 1.3v.3L8 9l6.5-4.4v-.3zm0 2.1v5.1h13V6.4L8 10.8z"/></svg>info@varnok-fs.ch</li>
      <li><svg viewBox="0 0 16 16"><path d="M8 0a8 8 0 1 0 0 16A8 8 0 0 0 8 0zm-1 2.2c-.6 1-2.5 1.3-2.8 2.6-.3 1.4 1.5 1.3 2.3 2.2.8 1 0 2.3.8 3.3.6.8 1.4 2 1 3.5A6 6 0 0 1 2.1 7.3 6 6 0 0 1 7 2.2zm4.6 1.5A6 6 0 0 1 14 8c0 1.2-.3 2.3-.9 3.2-.5-1-.4-2.5-1.6-3-1.1-.4-1.8.6-2.6-.2-.7-.7.4-1.6 1.1-2 .7-.5 1.8-1.1 1.6-2.3z"/></svg>www.varnok-fs.ch</li>
    </ul>
    <address class="company-address">
      Varnok Facility Services Tulbrecht<br>
      Kirchmattweg 12<br>
      6331 Cham
    </address>
  </section>

  <section class="card card-back">
    <p class="brand-name">Varnok Facility Services</p>

    <div class="service" style="left:105px">
      <span class="service-icon" role="img" aria-label="Broom icon">
        <svg viewBox="0 0 48 48"><rect x="22" y="2" width="4" height="26" rx="2"/><path d="M19 27h10l2 5H17z"/><path d="M17 32h14l5 14H12z"/></svg>
      </span>Cleaning</div>

    <div class="service" style="left:224px">
      <span class="service-icon" role="img" aria-label="Key icon">
        <svg viewBox="0 0 48 48"><path d="M16 6a10 10 0 1 0 0 20 10 10 0 0 0 0-20zm0 6a4 4 0 1 1 0 8 4 4 0 0 1 0-8z"/><path d="M22 22l4-4 18 18v6h-6v-4h-4v-4h-4z"/></svg>
      </span>Caretaking</div>

    <div class="service" style="left:359px">
      <span class="service-icon" role="img" aria-label="Spray bottle icon">
        <svg viewBox="0 0 48 48"><path d="M14 4h16l6 4v4h-6l-2-2h-6v6h4v4H14v-4h4v-6h-4z"/><path d="M12 22h20l2 6v16a2 2 0 0 1-2 2H12a2 2 0 0 1-2-2V28z"/></svg>
      </span>Maintenance cleaning</div>

    <div class="service" style="left:486px">
      <span class="service-icon" role="img" aria-label="Bucket icon">
        <svg viewBox="0 0 48 48"><path d="M10 14a14 10 0 0 1 28 0h-3a11 7 0 0 0-22 0z"/><path d="M8 16h32l-4 28H12z"/><rect x="22" y="2" width="4" height="16" rx="2" transform="rotate(20 24 10)"/></svg>
      </span>Industrial cleaning</div>

    <div class="service" style="left:605px">
      <span class="service-icon" role="img" aria-label="Watering can icon">
        <svg viewBox="0 0 48 48"><path d="M16 18h20v22a2 2 0 0 1-2 2H18a2 2 0 0 1-2-2z"/><path d="M36 20a7 7 0 0 1 0 14v-4a3 3 0 0 0 0-6z"/><path d="M16 24L4 14l-2 2 12 14z"/><path d="M20 10h12v4H20z"/><rect x="0" y="10" width="6" height="6" rx="1"/></svg>
      </span>Gardening</div>

    <div class="service" style="left:719px">
      <span class="service-icon" role="img" aria-label="Waste bin icon">
        <svg viewBox="0 0 48 48"><path d="M6 8h36v6H6z"/><path d="M20 3h8v4h-8z"/><path d="M9 16h30l-3 28H12z"/></svg>
      </span>Disposal</div>
  </section>

</div>
</body>
</html>
```